Harlowick billboard

Looking to change up a current design

Remove the best pricing in Sevier county

Remove the prices
Make it say 16/20/30/40 yard dumpsters

Remove delivery pick up 7 days a week

Keep current colors

```html
<!DOCTYPE html>
<html lang="en">
<head>
<meta charset="utf-8">
<title>Harlowick Dumpsters Billboard</title>
<link href="https://fonts.googleapis.com/css2?family=Montserrat:wght@500;700;800;900&display=swap" rel="stylesheet">
<style>
  :root{
    --page:#d7d7d9;
    --night:#1b1b1c;
    --night-soft:#3a3a3b;
    --ink:#1f1f20;
    --purple:#6a2f9c;
    --purple-pill:#7b48a8;
    --white:#ffffff;
  }
  *{margin:0;padding:0;box-sizing:border-box}
  html,body{width:1198px;height:1200px;overflow:hidden;background:var(--page)}
  body{font-family:"Montserrat",sans-serif;position:relative}
  .billboard{
    position:absolute;left:39px;top:423px;width:1120px;height:353px;
    overflow:hidden;box-shadow:0 18px 30px rgba(0,0,0,.18);
  }
  .backdrop-photo{
    position:absolute;inset:0;
    background:linear-gradient(180deg,#262627 0%,var(--night) 45%,var(--night-soft) 100%);
  }
  .brand{
    position:absolute;left:140px;top:30px;width:332px;
    color:var(--white);font-weight:800;text-transform:uppercase;
    display:flex;flex-direction:column;align-items:center;line-height:1;
  }
  .brand-name{font-size:56px;letter-spacing:1px}
  .brand-sub{font-size:27px;letter-spacing:2px;margin-top:4px;align-self:flex-end}
  .offers{
    position:absolute;left:18px;top:152px;width:604px;
    display:grid;grid-template-columns:repeat(4,1fr);
  }
  .offer{text-align:center;color:var(--white);text-transform:uppercase;line-height:1}
  .offer-size{
    font-size:30px;font-weight:900;
    text-shadow:-2px -2px 0 var(--purple),2px -2px 0 var(--purple),-2px 2px 0 var(--purple),2px 2px 0 var(--purple),0 3px 0 var(--purple);
  }
  .offer-kind{font-size:21px;font-weight:800;margin-top:7px}
  .offer-note{font-size:14px;font-weight:500;margin-top:6px;letter-spacing:.5px}
  .paper-strip{position:absolute;left:0;top:250px;width:730px;height:103px}
  .web{
    position:absolute;left:40px;top:294px;z-index:2;
    font-size:33px;font-weight:800;color:var(--ink);letter-spacing:.2px;white-space:nowrap;
  }
  .truck-photo{
    position:absolute;left:650px;top:97px;width:430px;height:252px;
    background:linear-gradient(100deg,#e9e9ea 0%,#cfcfd2 38%,#4a2a6a 62%,#5b2f88 85%,#2b2b2d 100%);
    border-radius:6px;
  }
  .phone{
    position:absolute;left:836px;top:299px;width:281px;height:37px;z-index:2;
    background:var(--purple-pill);color:var(--white);
    display:flex;align-items:center;justify-content:center;gap:8px;
    font-size:29px;font-weight:700;
  }
  .phone svg{width:18px;height:18px}
</style>
</head>
<body>
  <section class="billboard">
    <div class="backdrop-photo" role="img" aria-label="Dark black-and-white photo of trees and a lot behind the truck"></div>

    <div class="brand">
      <span class="brand-name">Harlowick</span>
      <span class="brand-sub">Dumpsters</span>
    </div>

    <div class="offers">
      <div class="offer">
        <div class="offer-size">16-Yard</div>
        <div class="offer-kind">Dumpsters</div>
        <div class="offer-note">Starting at</div>
      </div>
      <div class="offer">
        <div class="offer-size">20-Yard</div>
        <div class="offer-kind">Dumpsters</div>
        <div class="offer-note">Starting at</div>
      </div>
      <div class="offer">
        <div class="offer-size">30-Yard</div>
        <div class="offer-kind">Dumpsters</div>
        <div class="offer-note">Starting at</div>
      </div>
      <div class="offer">
        <div class="offer-size">40-Yard</div>
        <div class="offer-kind">Dumpsters</div>
        <div class="offer-note">Starting at</div>
      </div>
    </div>

    <svg class="paper-strip" viewBox="0 0 730 103" preserveAspectRatio="none" aria-hidden="true">
      <defs>
        <linearGradient id="paperFade" x1="0" x2="1" y1="0" y2="0">
          <stop offset="0" stop-color="#fff"/>
          <stop offset=".86" stop-color="#fff"/>
          <stop offset="1" stop-color="#fff" stop-opacity="0"/>
        </linearGradient>
      </defs>
      <path fill="#bdbdbd" d="M0 12 L18 9 L34 13 L52 8 L70 12 L92 10 L110 14 L132 9 L150 13 L172 10 L196 14 L220 9 L244 12 L270 8 L296 13 L320 10 L346 12 L372 8 L398 13 L424 10 L452 12 L480 8 L506 13 L532 10 L560 12 L588 9 L616 13 L642 10 L670 12 L700 10 L730 12 L730 103 L0 103 Z"/>
      <path fill="url(#paperFade)" d="M0 16 L16 14 L30 18 L48 13 L66 17 L88 15 L108 19 L128 14 L148 18 L170 15 L194 19 L218 14 L242 17 L268 13 L294 18 L318 15 L344 17 L370 13 L396 18 L422 15 L450 17 L478 13 L504 18 L530 15 L558 17 L586 14 L614 18 L640 15 L668 17 L698 15 L730 17 L730 103 L0 103 Z"/>
    </svg>

    <div class="web">HARLOWICKDUMPSTERS.COM</div>

    <div class="truck-photo" role="img" aria-label="Photo of a white roll-off truck carrying a purple dumpster"></div>

    <div class="phone">
      <svg viewBox="0 0 24 24" aria-hidden="true"><path fill="#fff" d="M6.6 10.8a15.1 15.1 0 0 0 6.6 6.6l2.2-2.2c.3-.3.7-.4 1-.2 1.1.4 2.3.6 3.6.6.6 0 1 .4 1 1V20c0 .6-.4 1-1 1A17 17 0 0 1 3 4c0-.6.4-1 1-1h3.5c.6 0 1 .4 1 1 0 1.3.2 2.5.6 3.6.1.3 0 .7-.2 1z"/></svg>
      <span>865-555-0142</span>
    </div>
  </section>
</body>
</html>
```